New Stationery New Logo for KT Fabrication Limited

We have a new logo and now want new stationary to go with it

This will be

Letterhead
Compliments Slip
Business Cards

Company details are
KT Fabrication Limited
Dellmoor Road, Halvercombe, Westmarsh, CV34 7HX, UK
Telephone : +44(0)1632 960617
Fax: +44(0)1632 960928
Email: sales@ktfabrication.co.uk
Web: www.ktfabrication.co.uk

Target Market(s)

Engineering / Metal Stamping

Industry/Entity Type

Manufacture

Contact Information for Business Card

Colin Brearley
Business Development Manager
KT Fabrication Limited
Dellmoor Road
Halvercombe
Westmarsh
CV34 7HX, UK

T: +44(0)1632 960617
F: +44(0)1632 960928
E: sales@ktfabrication.co.uk
W: www.ktfabrication.co.uk

Font styles to use
Sans Serif

Colors
33a6d7
0555a3
3176b5
85cae6
85acd3

Requirements
Must have
• Logo

```html
<!DOCTYPE html>
<html lang="en">
<head>
<meta charset="utf-8">
<title>KT Fabrication Limited – Stationery</title>
<link rel="stylesheet" href="https://fonts.googleapis.com/css2?family=Arimo:wght@400;700&family=PT+Serif&display=swap">
<style>
  :root {
    --ink: #111111;
    --navy: #1d2f7a;
    --brand-blue: #0f5fa8;
    --brand-soft: #85acd3;
    --pale-blue: #b1c3e1;
    --watermark: #e8e8ec;
    --bar: #0b0f12;
    --gear-grey: #d9d9d9;
    --white: #ffffff;
  }
  * { margin: 0; padding: 0; box-sizing: border-box; }
  html, body { width: 1200px; height: 1200px; overflow: hidden; background: var(--white); }
  body { font-family: "Arimo", Arial, sans-serif; color: var(--ink); position: relative; }

  .icon { width: 15px; height: 15px; fill: none; stroke: currentColor; stroke-width: 1.8; stroke-linecap: round; stroke-linejoin: round; flex: none; }

  /* Letterhead */
  .letterhead-name {
    position: absolute; left: 356px; top: 90px; width: 190px; text-align: center;
    font-weight: 700; font-size: 16px; letter-spacing: 4px; color: var(--navy); white-space: nowrap;
  }
  .letterhead-contact { position: absolute; left: 582px; top: 24px; font-size: 15px; line-height: 1; }
  .letterhead-contact .row { display: flex; gap: 12px; align-items: flex-start; margin-bottom: 2px; }
  .letterhead-contact .row span { line-height: 22px; }
  .letterhead-contact .icon { margin-top: 3px; }

  .watermark-name {
    position: absolute; left: 416px; width: 320px; top: 250px; text-align: center;
    font-weight: 700; font-size: 190px; letter-spacing: 10px; color: var(--watermark);
  }

  .footer-bar {
    position: absolute; left: 340px; top: 642px; width: 476px; height: 36px;
    background: var(--bar); color: var(--white); font-size: 17px;
    display: flex; align-items: center; padding: 0 10px;
  }
  .footer-bar .item { display: flex; align-items: center; gap: 10px; }
  .footer-bar .item.fax { margin-left: auto; font-size: 15.5px; margin-right: 28px; }

  /* Compliments slip */
  .slip-shadow { position: absolute; left: 84px; top: 715px; width: 610px; height: 199px; background: var(--brand-soft); }
  .slip-panel {
    position: absolute; left: 64px; top: 691px; width: 610px; height: 198px;
    background: var(--brand-blue); color: var(--white); font-size: 19.5px; padding: 11px 0 0 20px;
  }
  .slip-panel .row { display: flex; align-items: center; gap: 17px; height: 31.7px; }
  .slip-panel .icon { width: 16px; height: 16px; }

  .gear-art {
    position: absolute; left: 64px; top: 914px; width: 368px; height: 286px;
    background: radial-gradient(circle at 40% 60%, var(--gear-grey), #ececec 55%, var(--white) 100%);
    opacity: 0.8;
  }
  .pixel-art {
    position: absolute; left: 861px; top: 691px; width: 276px; height: 182px;
    background: linear-gradient(135deg, var(--pale-blue), #dbe4f2);
    opacity: 0.75;
  }
  .slip-name {
    position: absolute; left: 727px; top: 982px; width: 400px; text-align: center;
    font-weight: 700; font-size: 29px; letter-spacing: 7px; color: var(--navy); white-space: nowrap;
  }
  .slip-rule { position: absolute; left: 94px; top: 1146px; width: 652px; height: 6px; background: var(--ink); }
  .slip-title {
    position: absolute; left: 749px; top: 1114px;
    font-family: "PT Serif", Georgia, serif; font-size: 33px; color: var(--brand-blue); white-space: nowrap;
  }
</style>
</head>
<body>
<svg width="0" height="0" style="position:absolute" aria-hidden="true">
  <defs>
    <symbol id="i-pin" viewBox="0 0 16 16"><path d="M8 15s5-5 5-9A5 5 0 0 0 3 6c0 4 5 9 5 9z"/><circle cx="8" cy="6" r="1.8"/></symbol>
    <symbol id="i-phone" viewBox="0 0 16 16"><path d="M4 1.5l2.3 3-1.4 1.6c.8 2 2.3 3.6 4.3 4.6l1.5-1.4 3 2.3-1.5 2.4C7 13.5 2.5 9 2 3z"/></symbol>
    <symbol id="i-fax" viewBox="0 0 16 16"><rect x="4" y="1.5" width="8" height="5"/><rect x="1.5" y="6.5" width="13" height="7.5" rx="1"/><path d="M5 10.5h6"/></symbol>
    <symbol id="i-globe" viewBox="0 0 16 16"><circle cx="8" cy="8" r="6.5"/><path d="M1.5 8h13M8 1.5c-3 3.5-3 9.5 0 13M8 1.5c3 3.5 3 9.5 0 13"/></symbol>
    <symbol id="i-mail" viewBox="0 0 16 16"><rect x="1.5" y="3.5" width="13" height="9"/><path d="M1.5 3.5L8 9l6.5-5.5"/></symbol>
  </defs>
</svg>

<section class="letterhead">
  <div class="letterhead-name">KT FABRICATION</div>
  <div class="letterhead-contact">
    <div class="row"><svg class="icon"><use href="#i-pin"/></svg><span>Dellmoor Road, Halvercombe,<br>Westmarsh, CV34 7HX, UK</span></div>
    <div class="row"><svg class="icon"><use href="#i-phone"/></svg><span>+44(0)1632 960617</span></div>
    <div class="row"><svg class="icon"><use href="#i-mail"/></svg><span>sales@ktfabrication.co.uk</span></div>
  </div>
  <div class="watermark-name" aria-hidden="true">KT</div>
  <div class="footer-bar">
    <div class="item"><svg class="icon"><use href="#i-globe"/></svg><span>www.ktfabrication.co.uk</span></div>
    <div class="item fax"><svg class="icon"><use href="#i-fax"/></svg><span>+44(0)1632 960928</span></div>
  </div>
</section>

<section class="compliments-slip">
  <div class="slip-shadow"></div>
  <div class="slip-panel">
    <div class="row"><svg class="icon"><use href="#i-pin"/></svg><span>Dellmoor Road, Halvercombe, Westmarsh, CV34 7HX, UK</span></div>
    <div class="row"><svg class="icon"><use href="#i-phone"/></svg><span>+44(0)1632 960617</span></div>
    <div class="row"><svg class="icon"><use href="#i-fax"/></svg><span>+44(0)1632 960928</span></div>
    <div class="row"><svg class="icon"><use href="#i-globe"/></svg><span>sales@ktfabrication.co.uk</span></div>
    <div class="row"><svg class="icon"><use href="#i-mail"/></svg><span>www.ktfabrication.co.uk</span></div>
  </div>
  <div class="gear-art" role="img" aria-label="Faint grey illustration of interlocking gears"></div>
  <div class="pixel-art" role="img" aria-label="Scattered pale blue square pixel pattern"></div>
  <div class="slip-name">KT FABRICATION</div>
  <div class="slip-rule"></div>
  <div class="slip-title">With Compliments</div>
</section>
</body>
</html>
```